Letterhead to Introduce a 'Sister' Company.

What I am needing is a design for a letter head to introduce our current customers base of (KT Alarm) customers to our new service, 'Kestrel Tide Solar Brokers'

```html
<!DOCTYPE html>
<html lang="en">
<head>
<meta charset="utf-8">
<title>Kestrel Tide Solar Brokers – Letterhead</title>
<link rel="stylesheet" href="https://fonts.googleapis.com/css2?family=Arimo:wght@400;700&display=swap">
<style>
  :root {
    --navy: #0f4578;
    --orange: #f39b1c;
    --ink: #555555;
    --paper: #ffffff;
    --backdrop: #e9e9e9;
  }
  * { margin: 0; padding: 0; box-sizing: border-box; }
  html, body {
    width: 1200px;
    height: 1200px;
    overflow: hidden;
    background: var(--backdrop);
    font-family: "Arimo", Arial, sans-serif;
  }
  .letterhead {
    position: absolute;
    left: 150px;
    top: 50px;
    width: 900px;
    height: 1100px;
    background: var(--paper);
  }
  .brand {
    position: absolute;
    left: 58px;
    top: 78px;
    display: flex;
    align-items: center;
    gap: 12px;
  }
  .brand-dot {
    width: 34px;
    height: 34px;
    border-radius: 50%;
    background: var(--orange);
    flex: none;
  }
  .brand-name {
    color: var(--navy);
    font-weight: 700;
    font-size: 21px;
    line-height: 1.15;
    letter-spacing: 0.3px;
    text-transform: uppercase;
  }
  .rule {
    position: absolute;
    top: 154px;
    height: 9px;
  }
  .rule-main { left: 58px; width: 581px; background: var(--navy); }
  .rule-accent { left: 651px; width: 199px; background: var(--orange); }
  .contact {
    position: absolute;
    left: 651px;
    top: 83px;
    list-style: none;
    color: var(--ink);
    font-size: 16px;
    line-height: 19px;
  }
  .contact li {
    display: flex;
    align-items: center;
    gap: 6px;
  }
  .contact svg {
    width: 15px;
    height: 15px;
    fill: var(--navy);
    flex: none;
  }
</style>
</head>
<body>
  <main class="letterhead">
    <header>
      <div class="brand">
        <span class="brand-dot"></span>
        <div class="brand-name">Kestrel Tide<br>Solar Brokers</div>
      </div>
      <ul class="contact">
        <li>
          <svg viewBox="0 0 16 16" aria-hidden="true"><path d="M1 3h14v10H1z M1.6 3.4 8 8.6l6.4-5.2" fill="var(--navy)" stroke="#fff" stroke-width="1"/></svg>
          hello@kestreltide.com
        </li>
        <li>
          <svg viewBox="0 0 16 16" aria-hidden="true"><path d="M3.6 1.2 6 3.8 4.9 5.6c.9 2 2.5 3.6 4.5 4.5l1.8-1.1 2.6 2.4-1.3 2.4C7.400 13.600 2.400 8.600 1.200 2.500z"/></svg>
          5550-142-387
        </li>
        <li>
          <svg viewBox="0 0 16 16" aria-hidden="true"><circle cx="8" cy="8" r="7"/><path d="M1 8h14M8 1c-2.6 3-2.6 11 0 14M8 1c2.6 3 2.6 11 0 14" fill="none" stroke="#fff" stroke-width="1"/></svg>
          kestreltide.com
        </li>
      </ul>
      <div class="rule rule-main"></div>
      <div class="rule rule-accent"></div>
    </header>
  </main>
</body>
</html>
```